Peter + Rob's 30th Birthday FB event cover photo

We're after a Facebook even cover photo for our 30th B'day. We live in Sydney
Peter + Rob's 30th Birthday

Venue (these details can be used in the graphic):
Quiet Heron
the basement of
The Marlow Hotel
42 Brackley St Fernhill
2 August 8pm-3am

The Marlow logo: http://www.themarlowhotelqz.com
Quiet Heron logo: http://quietheronpurrqz.com.au
The horizontal FaceBook cover photo for events has specific dimensions
As ideas I kind of like the styling of the dj poster (file attached) as a rough guide but not essential (i.e. no need to stick to that format/colours/dark shades) and Also the poster Pixel Harbour's Bruno did for Lumen Run
Thanks!

```html
<!DOCTYPE html>
<html lang="en">
<head>
<meta charset="utf-8">
<title>Peter &amp; Rob's 30th Birthday</title>
<link rel="stylesheet" href="https://fonts.googleapis.com/css2?family=Quicksand:wght@400;700&display=swap">
<style>
  :root {
    --bg-deep: #3a1710;
    --bg-mid: #7a3422;
    --bg-warm: #b8583a;
    --bg-glow: #e08a62;
    --title: #f4d6c2;
    --detail: #c98a72;
    --date: #ec7a4e;
    --venue: #d9391d;
  }
  html, body {
    margin: 0;
    padding: 0;
    overflow: hidden;
    background: var(--bg-deep);
  }
  .cover {
    position: relative;
    width: 1200px;
    height: 443px;
    overflow: hidden;
    font-family: "Quicksand", sans-serif;
    text-transform: uppercase;
  }
  .cover__backdrop {
    position: absolute;
    inset: 0;
    background:
      radial-gradient(ellipse 40% 70% at 100% 10%, var(--bg-glow) 0%, transparent 70%),
      radial-gradient(ellipse 35% 60% at 88% 95%, var(--bg-warm) 0%, transparent 75%),
      radial-gradient(ellipse 45% 60% at 0% 100%, var(--bg-warm) 0%, transparent 80%),
      radial-gradient(ellipse 60% 80% at 55% 45%, var(--bg-deep) 0%, transparent 80%),
      linear-gradient(120deg, var(--bg-warm) 0%, var(--bg-mid) 35%, var(--bg-deep) 65%, var(--bg-mid) 100%);
  }
  .cover__title {
    position: absolute;
    left: 33px;
    top: 30px;
    margin: 0;
    color: var(--title);
    font-weight: 700;
    font-size: 80px;
    line-height: 96px;
    letter-spacing: 4px;
  }
  .cover__address {
    position: absolute;
    left: 35px;
    top: 229px;
    margin: 0;
    color: var(--detail);
    font-weight: 400;
    font-size: 17px;
    letter-spacing: 1px;
    word-spacing: 2px;
    white-space: pre;
  }
  .cover__date {
    position: absolute;
    left: 33px;
    top: 252px;
    margin: 0;
    color: var(--date);
    font-weight: 700;
    font-size: 38px;
    letter-spacing: 2px;
  }
  .cover__venue {
    position: absolute;
    right: 40px;
    top: 380px;
    margin: 0;
    color: var(--venue);
    font-weight: 700;
    font-size: 30px;
    letter-spacing: 3px;
  }
</style>
</head>
<body>
  <main class="cover">
    <div class="cover__backdrop" role="img" aria-label="Abstract background of overlapping translucent rust and orange paper squares"></div>
    <h1 class="cover__title">Peter &amp; Rob's<br>30th Birthday</h1>
    <p class="cover__address">42 Brackley St Fernhill    The basement of The Marlow Hotel</p>
    <p class="cover__date">2 August 8pm - 3am</p>
    <p class="cover__venue">Quiet Heron</p>
  </main>
</body>
</html>
```